LITTLE DESIGN WORK REQUIRED!

UPDATE: WE WEREN'T OVERLY ECSTATIC WITH THE DESIGNS WE WERE RECEIVING SO WE DID MOST OF THE DESIGN WORK OURSELVES...

PLEASE SEE THE NEWLY ATTACHED PPT DOC TO VIEW NEARLY EXACT REPLICAS OF WHAT WE WANT THE SITE TO LOOK LIKE. WE NOW NEED YOUR HELP TO MAKE IT LOOK LIKE SOMETHING WORTHY OF THE WEB.

NO CODING REQUIRED - EXPECTED OUTPUT PSD FILES

Hi everyone!

We're looking for a designer to work their magic for our site! We're a not-for-profit program aimed at helping young people realise their potential!

In the attached PPT file, you'll notice we've already DESIGNED THE ENTIRE SITE IN POWERPOINT. Now, we need YOU to make the small changes we requested in the document as well as design the whole thing in psd.

Any questions, don't hesitate to ask.

Brook-Rise
Updates

We've done about 95% of the design for you. Please fine-tune it. See the newly attached PPT doc for details. 

The best two designs will win. This project closes on Friday - please message us if you are absolutely sure you cannot make the deadline.

Thanks,
Brook-Rise

```html
<!DOCTYPE html>
<html lang="en">
<head>
<meta charset="utf-8">
<title>Brook-Rise — Website Mainpage</title>
<link href="https://fonts.googleapis.com/css2?family=Caladea:wght@400;700&family=PT+Sans:ital,wght@0,400;0,700;1,400&display=swap" rel="stylesheet">
<style>
:root{
  --outer:#e6e6e6;
  --page:#ffffff;
  --ink:#222222;
  --text:#555555;
  --muted:#888888;
  --green:#5fb31f;
  --green-dark:#3f8a12;
  --green-light:#8fd04a;
  --blue:#1f67b1;
  --blue-light:#4a8fd6;
  --orange:#e0780f;
  --red:#d8450c;
  --archive:#4fb81c;
  --gold:#f0a800;
  --footer:#2b2b2b;
  --footer-deep:#161616;
  --footer-text:#c9c9c9;
  --rule:#dddddd;
}
*{box-sizing:border-box;margin:0;padding:0}
html,body{width:1200px;height:2796px;overflow:hidden}
body{background:var(--outer);font-family:"PT Sans",Arial,sans-serif;color:var(--text);position:relative}
.abs{position:absolute}
.page{position:absolute;left:22px;top:0;width:1156px;height:2505px;background:var(--page);box-shadow:0 0 18px rgba(0,0,0,.18)}

/* header */
.connect{left:876px;top:0;width:266px;height:51px;background:#e9e9e9;border-radius:0 0 8px 8px;display:flex;align-items:center;padding-left:26px;gap:8px;font-size:17px;font-weight:700;color:#666}
.connect .social{display:flex;gap:6px;margin-left:14px}
.connect .social span{width:22px;height:22px;border-radius:4px;background:var(--blue-light)}
.logo{left:65px;top:100px;display:flex;align-items:center;gap:14px}
.logo .dot{width:58px;height:58px;border-radius:50%;background:var(--green)}
.logo .name{font-family:"PT Sans",sans-serif;font-weight:700;font-size:54px;color:var(--ink);letter-spacing:-1px}
.quote{left:800px;top:92px;width:330px;font-style:italic;color:#777;font-size:22px;line-height:29px}
.quote .mark{font-family:Caladea,serif;font-size:40px;color:#bbb;vertical-align:-12px;font-style:normal}
.quote cite{display:block;font-size:16px;margin-left:16px}

/* nav */
.nav{left:40px;top:224px;width:1118px;height:60px;background:linear-gradient(#7cc63a,#4f9e16);border:2px solid #3f8a12;display:flex}
.nav a{color:#fff;text-decoration:none;font-size:19px;display:flex;align-items:center;justify-content:center;border-right:1px solid rgba(255,255,255,.35)}
.nav a.active{background:linear-gradient(#2f6d0c,#245a08)}
.nav a:nth-child(1){width:124px}.nav a:nth-child(2){width:163px}.nav a:nth-child(3){width:151px}
.nav a:nth-child(4){width:163px}.nav a:nth-child(5){width:203px}.nav a:nth-child(6){width:89px}

/* hero */
.hero-photo{left:42px;top:296px;width:766px;height:354px;background:linear-gradient(#cfd9d2 0%,#6f8a52 45%,#4f6a3a 70%,#7f9aa3 100%)}
.feats{left:813px;top:296px;width:345px;height:354px;background:linear-gradient(#67b624,#4b9614);border:5px solid #8fd04a;outline:2px solid #3f8a12;text-align:center;color:#fff;font-family:Caladea,serif}
.feats h2{font-size:60px;font-weight:400;letter-spacing:2px;margin-top:42px;line-height:1}
.feats .dots{width:270px;margin:14px auto;border-top:3px dotted rgba(255,255,255,.85)}
.feats p{font-size:33px;line-height:42px;margin-top:26px}

/* headings */
.h-serif{font-family:Caladea,serif;font-weight:700;color:var(--ink)}
.welcome{left:47px;top:672px;font-size:29px}
.welcome em{font-style:normal;color:var(--green)}
.intro{left:47px;top:712px;width:760px;font-size:13.5px;line-height:18.5px}
.recent{left:47px;top:902px;font-size:28px}

/* category bars and posts */
.cat{height:36px;color:#fff;font-weight:700;font-size:18px;padding-left:16px;display:flex;align-items:center}
.cat.discover{left:47px;top:948px;width:755px;background:linear-gradient(#3b86d4,#1a5ea6)}
.cat.design{left:51px;top:1324px;width:752px;background:linear-gradient(#f08d22,#d56c0a)}
.cat.build{left:56px;top:1713px;width:752px;background:linear-gradient(#ea5a1a,#c93c06)}
.cat.archive{left:51px;top:2097px;width:755px;background:linear-gradient(#62c82c,#44a615)}
.post{width:352px}
.post .thumb{height:212px;border:2px solid #cfcfcf;padding:4px;background:#fff}
.post .thumb div{width:100%;height:100%}
.post h3{font-size:19px;font-weight:400;color:var(--ink);margin-top:18px}
.post p{font-size:13.5px;line-height:19px;margin-top:6px}

/* sidebar */
.side-title{font-family:Caladea,serif;font-weight:700;color:var(--blue);font-size:25px}
.touch{left:827px;top:732px;width:333px;height:426px;border:2px solid #6a9fd8;border-radius:4px;overflow:hidden}
.touch header{height:41px;background:linear-gradient(#3f8bd8,#1d5fa6);color:#fff;font-size:17px;display:flex;align-items:center;padding-left:22px}
.touch ul{list-style:none;padding:12px 12px 0}
.touch li{display:flex;gap:14px;padding:12px 0 14px;border-bottom:1px solid var(--rule)}
.touch li:last-child{border-bottom:none}
.touch svg{flex:none;margin-top:2px}
.touch .msg{color:var(--blue);font-size:13.5px;line-height:18px}
.touch .date{color:#666;font-size:13px;margin-top:4px}
.popular{left:827px;top:1230px;width:333px;list-style:none}
.popular li{display:flex;gap:14px;padding:12px 10px 16px;border-bottom:1px solid var(--rule);background:linear-gradient(#fff,#f5f5f5);height:92px}
.popular .num{flex:none;width:28px;height:28px;border-radius:50%;border:1px solid #aaa;background:#eee;font-family:Caladea,serif;font-size:19px;color:#444;display:flex;align-items:center;justify-content:center}
.popular p{font-size:13.5px;line-height:18px}
.know{left:857px;top:1634px;font-family:Caladea,serif;font-weight:700;color:var(--ink);font-size:25px}
.know-rule{left:857px;top:1672px;width:300px;border-top:1px solid var(--rule)}
.profile{width:240px}
.profile .pic{height:256px;border:2px solid #dcdcdc}
.profile h4{font-size:20px;font-weight:400;color:var(--ink);margin-top:22px}
.profile p{font-size:13.5px;line-height:18px;margin-top:4px}
.profile .btn{display:inline-block;margin-top:8px;background:linear-gradient(#ffbe2a,#f09a00);color:#fff;font-size:14px;padding:4px 24px;border-radius:3px}

/* footer */
.footer{left:0;top:2505px;width:1200px;height:249px;background:radial-gradient(ellipse at 50% 0,#3a3a3a,var(--footer) 60%)}
.footer h5{position:absolute;font-weight:400;font-size:19px;color:#ddd}
.links{position:absolute;list-style:none;font-size:12.5px;font-style:italic;color:var(--footer-text)}
.links li{height:29px}
.search{left:496px;top:65px;width:288px;height:30px;background:#fff;border-radius:15px;font-size:13px;font-style:italic;color:#888;padding:7px 14px}
.search .go{position:absolute;right:-2px;top:-1px;width:32px;height:32px;border-radius:50%;background:var(--green);color:#fff;font-style:normal;font-size:12px;display:flex;align-items:center;justify-content:center}
.contact{left:874px;top:65px;font-size:12.5px;line-height:24px;color:var(--footer-text)}
.contact b{color:#fff}
.bottom{left:0;top:2754px;width:1200px;height:42px;background:var(--footer-deep);color:#bbb;font-size:12.5px;padding:13px 0 0 40px}
</style>
</head>
<body>
<div class="page"></div>

<header>
  <div class="abs connect">Get Connect
    <div class="social" aria-label="Social links"><span></span><span></span><span></span><span></span></div>
  </div>
  <div class="abs logo"><span class="dot"></span><span class="name">BROOK-RISE</span></div>
  <blockquote class="abs quote"><span class="mark">“</span>What would you do if you Knew you could not fail? <span class="mark">”</span><cite>-R. Halloway</cite></blockquote>
  <nav class="abs nav">
    <a class="active">Home</a><a>About Us</a><a>Resources</a><a>Workshops</a><a>Ambasssadors</a><a>Feats</a>
  </nav>
</header>

<section>
  <div class="abs hero-photo" role="img" aria-label="Photo of a herd of elephants walking along a grassy riverbank"></div>
  <div class="abs feats">
    <h2>FEATS</h2>
    <div class="dots"></div>
    <p>Challenges that<br>dare you to<br>push yourself.</p>
    <div class="dots"></div>
  </div>
</section>

<main>
  <h1 class="abs h-serif welcome">Welcome to <em>Brook-Rise</em> Website Mainpage</h1>
  <div class="abs intro">
    <p>E-Commerce is a major progress in technology that has changed the way in which the customers now purchase information, products and the services. It's the new way of providing an opportunity to make your products and services available in the global market 24 hours a day through Internet</p>
    <p>Brightfield eSolutions is specialized in handling advanced web projects and the ongoing projects that require permanent maintenance and support. We like challenges and do complete these challenge with expertise we like solving questions that arises in such projects as these helps us to grow also. When considering advanced web development project, finding the right answers to the hard questions is a challenge for any firm, it includes expertise and enables Brightfield eSolutions to specialize in advanced projects and ongoing projects that require permanent support and maintenance.</p>
  </div>

  <h2 class="abs h-serif recent">Recent Posts</h2>

  <div class="abs cat discover">Discover</div>
  <article class="abs post" style="left:51px;top:995px"><div class="thumb"><div role="img" aria-label="Close-up of a bright green leaf" style="background:radial-gradient(#9ad93a,#3f8a12)"></div></div><h3>Tittle goes here</h3><p>Static website are the which are usually been used and are benefited through the Professionals and Small Companies. The companies with fewer budgets</p></article>
  <article class="abs post" style="left:443px;top:995px"><div class="thumb"><div role="img" aria-label="Photo of a smiling child holding a book" style="background:linear-gradient(#e8e4dc,#d8b8a0 55%,#d23a7a)"></div></div><h3>Tittle goes here</h3><p>Static website are the which are usually been used and are benefited through the Professionals and Small Companies. The companies with fewer budgets</p></article>

  <div class="abs cat design">Design</div>
  <article class="abs post" style="left:55px;top:1373px"><div class="thumb"><div role="img" aria-label="Rendering of a modern glass building interior" style="background:linear-gradient(#b8c9e0,#e4e2dc 60%,#8a7a66)"></div></div><h3>Tittle goes here</h3><p>Static website are the which are usually been used and are benefited through the Professionals and Small Companies. The companies with fewer budgets</p></article>
  <article class="abs post" style="left:447px;top:1373px"><div class="thumb"><div role="img" aria-label="Illustration of curving futuristic towers" style="background:linear-gradient(#f2f2f2,#c8ccd0 70%,#9fb07a)"></div></div><h3>Tittle goes here</h3><p>Static website are the which are usually been used and are benefited through the Professionals and Small Companies. The companies with fewer budgets</p></article>

  <div class="abs cat build">Build</div>
  <article class="abs post" style="left:62px;top:1759px"><div class="thumb"><div role="img" aria-label="Photo of a dark modern kitchen interior" style="background:linear-gradient(#3a3a3a,#bdbdbd 60%,#e6e6e6)"></div></div><h3>Tittle goes here</h3><p>Static website are the which are usually been used and are benefited through the Professionals and Small Companies. The companies with fewer budgets</p></article>
  <article class="abs post" style="left:455px;top:1759px"><div class="thumb"><div role="img" aria-label="Photo of hands reviewing building plans on a desk" style="background:linear-gradient(#d9d9d9,#f2f2f2 50%,#b8b8b8)"></div></div><h3>Tittle goes here</h3><p>Static website are the which are usually been used and are benefited through the Professionals and Small Companies. The companies with fewer budgets</p></article>

  <div class="abs cat archive">Archive</div>
  <article class="abs post" style="left:55px;top:2145px"><div class="thumb"><div role="img" aria-label="Photo of coloured chalk on a classroom board" style="background:linear-gradient(#7d94a8,#5f6f7a 60%,#c9a45a)"></div></div><h3>Tittle goes here</h3><p>Static website are the which are usually been used and are benefited through the Professionals and Small Companies. The companies with fewer budgets</p></article>
  <article class="abs post" style="left:447px;top:2145px"><div class="thumb"><div role="img" aria-label="Photo of business people in a bright office" style="background:linear-gradient(#f4f4f4,#cfcfcf 60%,#2e2e2e)"></div></div><h3>Tittle goes here</h3><p>Static website are the which are usually been used and are benefited through the Professionals and Small Companies. The companies with fewer budgets</p></article>
</main>

<aside>
  <h2 class="abs side-title" style="left:830px;top:668px">Stay In Touch</h2>
  <div class="abs touch">
    <header>Get In Touch</header>
    <ul>
      <li><svg width="54" height="40" viewBox="0 0 54 40"><ellipse cx="27" cy="18" rx="25" ry="15" fill="#e4e4e4"/><ellipse cx="27" cy="17" rx="20" ry="11" fill="#3d6fe0"/><path d="M12 24 L6 34 L20 27Z" fill="#3d6fe0"/></svg><div><p class="msg">Static website are the which are usually been used and are benefited</p><p class="date">Posted On 05 March 2012</p></div></li>
      <li><svg width="54" height="40" viewBox="0 0 54 40"><ellipse cx="27" cy="18" rx="25" ry="15" fill="#e4e4e4"/><ellipse cx="27" cy="17" rx="20" ry="11" fill="#3d6fe0"/><path d="M12 24 L6 34 L20 27Z" fill="#3d6fe0"/></svg><div><p class="msg">Static website are the which are usually been used and are benefited</p><p class="date">Posted On 05 March 2012</p></div></li>
      <li><svg width="54" height="40" viewBox="0 0 54 40"><ellipse cx="27" cy="18" rx="25" ry="15" fill="#e4e4e4"/><ellipse cx="27" cy="17" rx="20" ry="11" fill="#3d6fe0"/><path d="M12 24 L6 34 L20 27Z" fill="#3d6fe0"/></svg><div><p class="msg">Static website are the which are usually been used and are benefited</p><p class="date">Posted On 05 March 2012</p></div></li>
      <li><svg width="54" height="40" viewBox="0 0 54 40"><ellipse cx="27" cy="18" rx="25" ry="15" fill="#e4e4e4"/><ellipse cx="27" cy="17" rx="20" ry="11" fill="#3d6fe0"/><path d="M12 24 L6 34 L20 27Z" fill="#3d6fe0"/></svg><div><p class="msg">Static website are the which are usually been used and are benefited</p><p class="date">Posted On 05 March 2012</p></div></li>
    </ul>
  </div>

  <h2 class="abs side-title" style="left:830px;top:1175px">Popular Posts</h2>
  <ol class="abs popular">
    <li><span class="num">1</span><p>We have learnt that designing is not only inclined to powerful imaginations but also focused and attractive</p></li>
    <li><span class="num">2</span><p>We have learnt that designing is not only inclined to powerful imaginations but also focused and attractive</p></li>
    <li><span class="num">3</span><p>We have learnt that designing is not only inclined to powerful imaginations but also focused and attractive</p></li>
    <li><span class="num">4</span><p>We have learnt that designing is not only inclined to powerful imaginations but also focused and attractive to expected viewers also.</p></li>
  </ol>

  <h2 class="abs know">Get to Know Us</h2>
  <div class="abs know-rule"></div>
  <div class="abs profile" style="left:867px;top:1694px"><div class="pic" role="img" aria-label="Image of a hand placing a jigsaw puzzle piece against a blue sky" style="background:linear-gradient(#3a78c8,#a9cbe8 60%,#e8f0f6)"></div><h4>John Doe</h4><p>To manage the static website HTML knowledge is the required. The simple website are also said</p><span class="btn">meet John</span></div>
  <div class="abs profile" style="left:867px;top:2088px"><div class="pic" role="img" aria-label="Image of business silhouettes in front of blue city towers" style="background:linear-gradient(#1f5fae,#8fc4ea 55%,#dfeef8)"></div><h4>John Doe</h4><p>To manage the static website HTML knowledge is the required. The simple website are</p><span class="btn">meet John</span></div>
</aside>

<footer class="abs footer">
  <h5 style="left:51px;top:35px">Quick Links</h5>
  <ul class="links" style="left:51px;top:80px"><li>Main page</li><li>About Company</li><li>Services Overview</li><li>Testimonials</li></ul>
  <ul class="links" style="left:189px;top:80px"><li>Get To Know</li><li>Recent Blogs &amp; news</li><li>Resources</li><li>Workshops</li></ul>
  <ul class="links" style="left:336px;top:76px"><li>Popular Posts</li><li>Stay In Touch</li></ul>
  <h5 style="left:505px;top:30px">Search here</h5>
  <div class="abs search">type your word here..<span class="go">GO</span></div>
  <h5 style="left:874px;top:30px">Contact Information</h5>
  <div class="abs contact"><b>Company Name here</b><br>N-12/30 Market Lane Road<br>Y Way Dunmore United States Zip Code 4402<br>Tele : (555) 010 2040<br>Email : hello@brookrise.org</div>
</footer>
<div class="abs bottom">Copyright © 2012 Company Name | All right reserved</div>
</body>
</html>
```